Occupational Therapist does home accessibility for disabled folks; needs business card design

We need a business card for a company in Portland, Oregon that specializes in making homes accessible, comfortable, and functional for people who are disabled or aging who would like to stay in THEIR home. Our medical background as Occupational Therapists allows us to translate the functional needs of the person into the recommendations for the design of the home remodel.

Target Market(s)

Elderly, children of elderly
People with disabilities, families of people with disabilities

Industry/Entity Type

Business

Contact Information for Business Card

Company name: HomeWise
Name: Danielle Reyes Crawford, OTR/L, CAPS, ECHM
Occupational Therapist, Home Modification & Accessibility Specialist
website: www.homewiseforyears.com
email: homewiseforyears@nestmail.example
phone: (503)218-4057
CCB #: 487315

Font styles to use
Sans Serif

Requirements
Must have
• My logo
• Easy to read font with contrasting background
• Please list the Services offered: Occupational Therapy, Home safety & accessibility assessments, Home modification consulting, project management
Nice to have
• Friendly, welcoming feel
Should not have
• Dark colored background

```html
<!DOCTYPE html>
<html lang="en">
<head>
<meta charset="utf-8">
<title>HomeWise Business Card</title>
<link href="https://fonts.googleapis.com/css2?family=Lato:wght@400;700&display=swap" rel="stylesheet">
<style>
  :root {
    --bg: #efeeec;
    --card-white: #ffffff;
    --slate: #4b4b4d;
    --orange: #c87124;
    --orange-bright: #e07f22;
    --text-light: #ffffff;
    --text-dark: #3c3c3c;
  }
  * { margin: 0; padding: 0; box-sizing: border-box; }
  html, body { width: 1138px; height: 1200px; overflow: hidden; }
  body {
    background: var(--bg);
    font-family: "Lato", sans-serif;
    position: relative;
  }
  .card {
    position: absolute;
    width: 670px;
    height: 384px;
    box-shadow: 0 4px 14px rgba(0,0,0,0.25);
    overflow: hidden;
  }
  .card-front { left: 218px; top: 198px; background: var(--card-white); }
  .card-back { left: 216px; top: 617px; height: 381px; background: var(--slate); }

  .front-shape { position: absolute; inset: 0; }

  .brand {
    position: absolute;
    display: flex;
    align-items: center;
    gap: 12px;
    font-weight: 700;
    letter-spacing: 0.5px;
  }
  .brand-mark { width: 22px; height: 22px; background: var(--orange); }
  .card-front .brand { left: 440px; top: 70px; font-size: 38px; color: var(--slate); }
  .card-back .brand { left: 0; right: 0; justify-content: center; top: 130px; font-size: 58px; color: var(--text-light); }
  .card-back .brand-mark { width: 32px; height: 32px; }

  .contact-block {
    position: absolute;
    left: 26px;
    top: 241px;
    color: var(--text-light);
  }
  .person-name { font-size: 20px; font-weight: 700; color: var(--orange-bright); }
  .person-name .credentials { font-size: 13px; font-weight: 400; color: var(--text-light); }
  .role { font-size: 16px; line-height: 19px; }
  .contact-list { list-style: none; margin-top: 9px; font-size: 16px; line-height: 18px; }
  .contact-list li { display: flex; align-items: center; gap: 5px; }
  .contact-list svg { width: 12px; height: 12px; fill: var(--orange-bright); }
  .license {
    position: absolute;
    left: 462px;
    top: 349px;
    font-size: 15px;
    color: var(--text-light);
  }

  .services-band {
    position: absolute;
    left: 0; right: 0;
    top: 289px;
    height: 70px;
    background: var(--card-white);
    text-align: center;
    padding-top: 5px;
  }
  .services-title { font-size: 16px; color: var(--orange-bright); line-height: 19px; }
  .services-list { font-size: 16px; color: var(--text-dark); line-height: 20px; }
</style>
</head>
<body>
  <section class="card card-front">
    <svg class="front-shape" viewBox="0 0 670 384" width="670" height="384" aria-hidden="true">
      <polygon points="0,218 360,144 670,380 670,384 0,384" fill="var(--orange)"/>
      <polygon points="0,232 360,160 670,384 0,384" fill="var(--slate)"/>
    </svg>
    <div class="brand"><span class="brand-mark"></span><span>HomeWise</span></div>
    <div class="contact-block">
      <p class="person-name">Danielle Reyes Crawford, <span class="credentials">OTR/L, CAPS, ECHM</span></p>
      <p class="role">Occupational Therapist</p>
      <p class="role">Home Modification &amp; Accessibility Specialist</p>
      <ul class="contact-list">
        <li><svg viewBox="0 0 12 12"><path d="M2.5 0.5 4.5 3 3.4 4.3c0.8 1.7 2.1 3 3.8 3.8L8.5 7l2.5 2-1.3 2.2C5 11 1 7 0.8 2.3z"/></svg>(503)218-4057</li>
        <li><svg viewBox="0 0 12 12"><path d="M0 2h12v8H0z M0.8 2.6 6 6.6l5.2-4z" fill-rule="evenodd"/></svg>homewiseforyears@nestmail.example</li>
        <li><svg viewBox="0 0 12 12"><path d="M6 0a6 6 0 1 0 0.01 0zM6 1.2c-1 1.2-1.5 2.8-1.5 4.8s0.5 3.6 1.5 4.8c1-1.2 1.5-2.8 1.5-4.8S7 2.4 6 1.2zM1.3 5.4h9.4v1.2H1.3z" fill-rule="evenodd"/></svg>www.homewiseforyears.com</li>
      </ul>
    </div>
    <p class="license">CCB #: 487315</p>
  </section>

  <section class="card card-back">
    <div class="brand"><span class="brand-mark"></span><span>HomeWise</span></div>
    <div class="services-band">
      <p class="services-title">Services we provide</p>
      <p class="services-list">Occupational Therapy, Home safety &amp; accessibility assessments</p>
      <p class="services-list">Home modification consulting, project management</p>
    </div>
  </section>
</body>
</html>
```